Film and TV production company

I have the logo already designed by craft nest. I just need the text and the logo attached to the business card. Maybe a small design on the back of the card or text.

Industry/Entity Type

film tv arts

Contact Information for Business Card

Brent Walcott Cinematographer-Director

Colors
F0912C
F2A743
F7CA91
FBE8D2
FDF5EE
EE7325
F08F49
F5BC92
FAE3D3
FDF4ED

Requirements
Must have
• www.bluewattlestudio.com.au my email address mail@bluewattlestudio.com.au my mobile number 0412573984
Nice to have
• Some kind of small art work on the back that ties in with the logo design attached
Should not have
• Must clean and simple

```html
<!DOCTYPE html>
<html lang="en">
<head>
<meta charset="utf-8">
<title>Brent Walcott — Business Card</title>
<link rel="stylesheet" href="https://fonts.googleapis.com/css2?family=Playfair+Display:wght@700;800&family=Lato:wght@400&display=swap">
<style>
  :root {
    --card-black: #000000;
    --deco-gold: #e2bf7f;
    --deco-gold-deep: #3a2e1b;
    --text-gold: #e4c07f;
  }
  * { margin: 0; padding: 0; box-sizing: border-box; }
  html, body {
    width: 1200px;
    height: 706px;
    overflow: hidden;
    background: var(--card-black);
  }
  .business-card {
    position: relative;
    width: 1200px;
    height: 706px;
    background: var(--card-black);
    color: var(--text-gold);
  }
  .deco-band {
    position: absolute;
    top: 0;
    left: 0;
    width: 1200px;
    height: 148px;
    display: block;
  }
  .card-name {
    position: absolute;
    top: 296px;
    left: 0;
    width: 1186px;
    text-align: center;
    font-family: "Playfair Display", Georgia, serif;
    font-weight: 800;
    font-size: 74px;
    line-height: 80px;
    letter-spacing: 0.5px;
    text-transform: uppercase;
  }
  .card-role {
    position: absolute;
    top: 408px;
    left: 0;
    width: 1210px;
    text-align: center;
    font-family: "Lato", Arial, sans-serif;
    font-weight: 400;
    font-size: 35px;
    line-height: 44px;
    letter-spacing: 10.5px;
    text-transform: uppercase;
  }
  .card-contacts {
    position: absolute;
    top: 489px;
    left: 0;
    width: 1196px;
    list-style: none;
    text-align: center;
    font-family: "Lato", Arial, sans-serif;
    font-weight: 400;
    font-size: 37px;
    line-height: 50.5px;
    letter-spacing: 0.6px;
  }
</style>
</head>
<body>
  <main class="business-card">
    <svg class="deco-band" viewBox="0 0 1200 148" role="img" aria-label="Gold art deco pattern of interlocking hexagons with fan rays along the top edge">
      <defs>
        <linearGradient id="deco-band-fill" x1="0" y1="0" x2="0" y2="1">
          <stop offset="0" stop-color="var(--deco-gold-deep)"/>
          <stop offset="1" stop-color="var(--card-black)"/>
        </linearGradient>
      </defs>
      <rect width="1200" height="148" fill="url(#deco-band-fill)"/>
    </svg>

    <h1 class="card-name">Brent Walcott</h1>
    <p class="card-role">Cinematographer-Director</p>

    <ul class="card-contacts">
      <li class="contact-phone">0412573984</li>
      <li class="contact-email">mail@bluewattlestudio.com.au</li>
      <li class="contact-web">www.bluewattlestudio.com.au</li>
    </ul>
  </main>
</body>
</html>
```